Business Card Design Project

I need some business cards with the logo you did for us (attached)
I am looking for a coulourful yet serious business card

We do market research
on the back I want the logo

on the front my name : Corinne Valdessa
position : Manager
address : Brumel Partners Sarl - 27 Rue des tanneurs
1475 Prévondy - Switzerland
corinne.valdessa@brumelpartners.example
Tel : +4122 604 37 95
Mob France :+33 671 42 5083
Mob Italy +39 347 268 5190

The tree of the logo could also be used alone

THE BACKGROUND COLOR ON THE FRONT HAS TO BE WHITE, ON THE BACK YU CAN TRY OHER COLOUR BUT HOMOGENEOUS (NOT EXPENSIVE TO PRINT)

Target Market(s)

multinational companies or other market research companies

Industry/Entity Type

Market Research

Requirements
Must have
• logo on the back
and all the info above

```html
<!DOCTYPE html>
<html lang="en">
<head>
<meta charset="utf-8">
<title>Brumel Partners – Business Card</title>
<link rel="stylesheet" href="https://fonts.googleapis.com/css2?family=Source+Sans+3:wght@400;600;700&display=swap">
<style>
  :root {
    --page: #ffffff;
    --crop: #9a9a9a;
    --ink: #333333;
    --brand-pink: #d2235f;
    --brand-red: #c0263f;
    --kraft: #c49a6c;
    --accent-tan: #c8925a;
    --mark-fill: #8bbf3f;
  }
  * { margin: 0; padding: 0; box-sizing: border-box; }
  html, body {
    width: 1200px; height: 927px; overflow: hidden;
    background: var(--page);
    font-family: "Source Sans 3", Arial, sans-serif;
    color: var(--ink);
  }
  .sheet { position: relative; width: 1200px; height: 927px; }
  .crop-marks { position: absolute; inset: 0; }
  .card { position: absolute; top: 328px; width: 378px; height: 222px; }
  .card--front { left: 177px; background: var(--page); }
  .card--back { left: 661px; background: var(--kraft); }

  .brand-small {
    position: absolute; left: 21px; top: 17px;
    font-size: 15px; font-weight: 400; color: var(--brand-pink);
    letter-spacing: 0.2px;
  }
  .brand-dot {
    position: absolute; left: 26px; top: 58px;
    width: 92px; height: 92px; border-radius: 50%;
    background: var(--mark-fill);
  }
  .contact {
    position: absolute; right: 11px; top: 104px;
    text-align: right; font-size: 11.5px; line-height: 15.5px;
  }
  .contact .name { font-weight: 700; }
  .contact .role { color: var(--accent-tan); }
  .contact .address { margin-top: 15px; }
  .mobiles {
    position: absolute; left: 20px; right: 11px; top: 192px;
    display: flex; justify-content: space-between;
    font-size: 11.5px; white-space: nowrap;
  }
  .mobiles b { font-weight: 700; }

  .brand-dot--back {
    position: absolute; left: 159px; top: 22px;
    width: 62px; height: 62px; border-radius: 50%;
    background: var(--mark-fill);
  }
  .brand-large {
    position: absolute; left: 0; right: 0; top: 86px;
    text-align: center;
    font-size: 33px; font-weight: 600; color: var(--brand-red);
    letter-spacing: -0.3px;
  }
  .side-label {
    position: absolute; top: 588px;
    font-family: Arial, Helvetica, sans-serif; font-size: 16px; color: #222;
  }
</style>
</head>
<body>
<div class="sheet">
  <svg class="crop-marks" width="1200" height="927" aria-hidden="true">
    <g stroke="var(--crop)" stroke-width="1">
      <line x1="177.5" y1="244" x2="177.5" y2="301"/>
      <line x1="555.5" y1="244" x2="555.5" y2="301"/>
      <line x1="661.5" y1="244" x2="661.5" y2="301"/>
      <line x1="1039.5" y1="244" x2="1039.5" y2="301"/>
      <line x1="177.5" y1="578" x2="177.5" y2="633"/>
      <line x1="555.5" y1="578" x2="555.5" y2="633"/>
      <line x1="661.5" y1="578" x2="661.5" y2="633"/>
      <line x1="1039.5" y1="578" x2="1039.5" y2="633"/>
      <line x1="94" y1="328.5" x2="150" y2="328.5"/>
      <line x1="94" y1="549.5" x2="150" y2="549.5"/>
      <line x1="580" y1="328.5" x2="636" y2="328.5"/>
      <line x1="580" y1="549.5" x2="636" y2="549.5"/>
      <line x1="1065" y1="328.5" x2="1120" y2="328.5"/>
      <line x1="1065" y1="549.5" x2="1120" y2="549.5"/>
    </g>
  </svg>

  <section class="card card--front" aria-label="Card front">
    <div class="brand-small">brumel partners</div>
    <div class="brand-dot"></div>
    <div class="contact">
      <div><span class="name">Corinne Valdessa</span>, <span class="role">Manager</span></div>
      <div>corinne.valdessa@brumelpartners.example</div>
      <div>+ 4122 604 37 95</div>
      <div class="address">
        <div>27 Rue des Tanneurs</div>
        <div>1475 Prévondy , Switzerland</div>
      </div>
    </div>
    <div class="mobiles">
      <span><b>Mob France :</b> + 33 671 42 5083</span>
      <span><b>Mob Italy:</b> &nbsp;+ 39 347 268 5190</span>
    </div>
  </section>

  <section class="card card--back" aria-label="Card back">
    <div class="brand-dot--back"></div>
    <div class="brand-large">brumel partners</div>
  </section>

  <div class="side-label" style="left:192px">FRONT</div>
  <div class="side-label" style="left:678px">BACK</div>
</div>
</body>
</html>
```